Buchcover-Design für Fachbuch
Tolle Entwürfe und ein sehr effiziente Zusammenarbeit. Können wir nur weiterempfehlen.
Zielgruppe
Unternehmensberatung im Thema Arbeitszeit. Wir haben ein Fachbuch zum Thema Arbeitszeit und Personaleinsatzplanung für Geschäftsführer, HR Mitarbeiter, Führungskräfte, Studenten und alle geschrieben, die sich o.g. Themen näher informieren möchten
Aufgabenstellung
Folgende Textelemente sollen zu sehen sein:
Autorennamen: Dr. Reinhold Kattner, Lothar Brenning
Titel: PLAN STARK Betrieb - Dienstzeiten und Schichtorganisation fair, rentabel und marktnah einrichten
Außerdem: Unter Mitwirkung von Prof. Anton K. Ruhland
Und: mit vielen Praxisbeispielen (ggf. als eine Art Plakette)
Auf der Rückseite soll ein Klappentext und 2 Zitate zu sehen sein:
Klappentext:
Die Welt verändert sich dramatisch. Digitalisierung, Fachkräftemangel, Wertewandel und nicht zuletzt Ausnahmezustände wie die Coronakrise stellen Unternehmen vor große Herausforderungen. Wie können Unternehmen flexibel und gleichzeitig wirtschaftlich, kunden- und mitarbeiterorientiert agieren?
Reinhold Kattner und Lothar Brenning sehen eine innovative Arbeitszeitgestaltung als entscheidenden Hebel an, um Unternehmen aller Branchen in schnelllebigen Märkten flexibel aufzustellen. Die Autoren beleuchten mit vielen Beispielen aus ihrer Beratungspraxis, warum Arbeitszeitsysteme dringend modernisiert werden müssen und welche Möglichkeiten Sie bereits heute haben, Arbeitszeit innovativ zu gestalten.
Sie erfahren alles Wissenswerte über klassische Modelle, wie z.B. Schichtplan, Gleitzeit, Vertrauensarbeitszeit, Zeitkontensystem und Teilzeit, über Workforce Management (Workforce Analytics, Personalbedarfsermittlung und Forecast, Personaleinsatzplanung, Zeiterfassung) bis hin zu Lebensarbeitszeit, Gruppenarbeit, Selbstorganisation, Homeoffice und New Work. Dabei lernen Sie nicht nur die Einzelkomponenten kennen, sondern erfahren auch, wie man diese geschickt zu einer für Mitarbeiter und Unternehmen gleichermaßen vorteilhaften Arbeitszeitsystematik kombiniert. Neben diesem strategischen Wissen vermitteln Ihnen die Autoren hilfreiche Methoden zur konkreten operativen Umsetzung dieser Themen.
Zitat 1:
„Durch die Weitergabe ihrer umfassenden Erfahrungen aus der Beratung ist es den Autoren in hervorragender Weise gelu..

```html
<!DOCTYPE html>
<html lang="de">
<head>
<meta charset="utf-8">
<title>PLAN STARK Betrieb – Buchumschlag</title>
<link rel="stylesheet" href="https://fonts.googleapis.com/css2?family=Roboto+Slab:wght@700&family=Roboto:ital,wght@0,300;0,400;0,500;1,400&family=Roboto+Condensed:wght@400&display=swap">
<style>
  :root {
    --navy: #1b1a85;
    --green: #79bd27;
    --white: #ffffff;
    --ink: #222222;
    --stage-dark: #666666;
    --stage-light: #d5d4d7;
    --photo-warm: #8a6a3e;
    --photo-cool: #d9d8dc;
    --photo-slate: #5c6266;
  }
  * { margin: 0; padding: 0; box-sizing: border-box; }
  html, body { width: 880px; height: 1200px; overflow: hidden; }
  body {
    position: relative;
    background: var(--stage-light);
    font-family: "Roboto", Arial, sans-serif;
  }
  .spread-band { position: absolute; left: 0; top: 0; width: 880px; height: 514px; background: var(--stage-dark); }
  .gap { position: absolute; left: 0; top: 514px; width: 880px; height: 27px; background: var(--white); }

  /* Back cover */
  .back-cover { position: absolute; left: 13px; top: 16px; width: 370px; height: 479px; background: var(--white); border: 1px solid #111; }
  .back-green { position: absolute; left: 0; top: 24px; width: 100%; height: 266px; background: var(--green); }
  .back-title { position: absolute; left: 0; top: 26px; width: 100%; text-align: center; font-family: "Roboto Slab", Georgia, serif; font-weight: 700; font-size: 25px; line-height: 23px; }
  .back-title .navy { color: var(--navy); }
  .back-title .light { color: var(--white); }
  .blurb { position: absolute; left: 48px; top: 100px; width: 274px; color: var(--white); font-size: 6.1px; line-height: 9.2px; text-align: justify; font-weight: 300; }
  .blurb p + p { margin-top: 9px; }
  .quote { position: absolute; right: 48px; text-align: right; font-size: 5.7px; line-height: 7.8px; color: var(--ink); font-weight: 500; }
  .quote-1 { top: 306px; width: 230px; }
  .quote-2 { top: 386px; width: 250px; }
  .quote cite { display: block; margin-top: 8px; color: var(--navy); font-style: italic; font-weight: 400; font-size: 5px; }
  .back-bar { position: absolute; left: 0; bottom: 8px; width: 100%; height: 16px; background: var(--navy); color: var(--white); font-size: 6.6px; line-height: 16px; text-align: right; padding-right: 14px; }

  /* Spine */
  .spine { position: absolute; left: 411px; top: 18px; width: 39px; height: 478px; background: var(--navy); border: 1px solid #8a8a9a; }
  .spine-text { position: absolute; left: 50%; white-space: nowrap; transform-origin: center; }
  .spine-authors { top: 72px; transform: translateX(-50%) rotate(-90deg); color: var(--white); font-size: 8.6px; font-weight: 500; }
  .spine-rule { position: absolute; left: 7px; top: 237px; width: 28px; height: 2px; background: var(--green); }
  .spine-title { top: 360px; transform: translateX(-50%) rotate(-90deg); color: var(--green); font-size: 11.4px; }

  /* Front cover */
  .front-cover { position: absolute; left: 489px; top: 16px; width: 370px; height: 479px; background: var(--white); border: 1px solid #888; overflow: hidden; }
  .photo { position: absolute; }
  .photo-factory { left: 0; top: 0; width: 186px; height: 151px; background: linear-gradient(135deg, #5a4a2e, var(--photo-warm) 45%, #b42a2a 70%, #2b2f3a); }
  .photo-clinic { left: 186px; top: 0; width: 184px; height: 151px; background: linear-gradient(160deg, #f2f1f3, var(--photo-cool) 60%, #c9a89c); }
  .photo-desk { left: 0; top: 290px; width: 370px; height: 189px; background: linear-gradient(160deg, #4b5257, var(--photo-slate) 45%, #7b8fb0 60%, #6a5e52); }
  .green-edge { position: absolute; left: 0; top: 0; width: 14px; height: 290px; background: var(--green); }
  .green-ladder { position: absolute; left: 0; top: 0; width: 14px; height: 151px; background: repeating-linear-gradient(to bottom, var(--green) 0 6px, #5c8f1d 6px 8px); }
  .blue-ladder { position: absolute; right: 0; top: 151px; width: 13px; height: 139px; background: repeating-linear-gradient(to bottom, var(--navy) 0 5px, var(--white) 5px 8px); }
  .title-block { position: absolute; left: 14px; top: 151px; width: 343px; height: 139px; background: var(--white); text-align: center; }
  .front-authors { margin-top: 13px; font-size: 9.6px; color: var(--ink); font-weight: 400; }
  .front-title { margin-top: 8px; font-family: "Roboto Slab", Georgia, serif; font-weight: 700; font-size: 25px; line-height: 23px; }
  .front-title .navy { color: var(--navy); }
  .front-title .green { color: var(--green); }
  .front-subtitle { margin-top: 8px; font-size: 11px; line-height: 17px; color: var(--ink); font-weight: 300; }
  .badge { position: absolute; left: 239px; top: 357px; width: 100px; height: 100px; }
  .badge-text { position: absolute; left: 239px; top: 392px; width: 100px; text-align: center; color: var(--white); font-style: italic; font-size: 9px; line-height: 11.5px; }
  .contributor { position: absolute; left: 33px; top: 457px; color: var(--white); font-size: 9.2px; font-weight: 300; }
</style>
</head>
<body>
  <div class="spread-band"></div>
  <div class="gap"></div>

  <section class="back-cover">
    <div class="back-green"></div>
    <h2 class="back-title"><span class="navy">PLAN STARK</span><br><span class="light">Betrieb</span></h2>
    <div class="blurb">
      <p><strong style="font-weight:400">Die Welt verändert sich dramatisch. Digitalisierung, Fachkräftemangel, Wertewandel und nicht zuletzt Ausnahmezustände wie die Coronakrise stellen Unternehmen vor große Herausforderungen. Wie können Unternehmen flexibel und gleichzeitig wirtschaftlich, kunden- und mitarbeiterorientiert agieren?</strong></p>
      <p>Sie erfahren alles Wissenswerte über klassische Modelle, wie z.B. Schichtplan, Gleitzeit, Vertrauensarbeitszeit, Zeitkontensystem und Teilzeit, über Workforce Management (Workforce Analytics, Personalbedarfsermittlung und Forecast, Personaleinsatzplanung, Zeiterfassung) bis hin zu Lebensarbeitszeit, Gruppenarbeit, Selbstorganisation, Homeoffice und New Work. Dabei lernen Sie nicht nur die Einzelkomponenten kennen, sondern erfahren auch, wie man diese geschickt zu einer für Mitarbeiter und Unternehmen gleichermaßen vorteilhaften Arbeitszeitsystematik kombiniert. Neben diesem strategischen Wissen vermitteln Ihnen die Autoren hilfreiche Methoden zur konkreten operativen Umsetzung dieser Themen.</p>
    </div>
    <blockquote class="quote quote-1">„Durch die Weitergabe ihrer umfassenden Erfahrungen aus der Beratung ist es den Autoren in hervorragender Weise gelungen, neue Einsichten und vertieftes Expertenwissen sowohl zur Implementierung von Workforce Management-Lösungen als auch zu konkreten Vorgehensweisen bei der Personaleinsatzplanung zu vermitteln.“
      <cite>Anton K. Ruhland | Professor für Personalmanagement an der Hochschule Bergfeld</cite>
    </blockquote>
    <blockquote class="quote quote-2">„Das vorliegende Buch von Kattner und Brenning liefert den entscheidenden Baustein zur Humanisierung von Ökonomie und Unternehmensorganisation und hat das Potenzial zu dem Standardwerk im Thema moderne Arbeitszeitgestaltung und Workforce Management zu werden.“
      <cite>Dr. Harald Menzing, Initiator des Kompetenznetzwerks Fachforum Plus &amp; Top 3 HR Influencer 2020 (Arbeitswelt Magazin)</cite>
    </blockquote>
    <div class="back-bar">Dr. Reinhold Kattner, Lothar Brenning</div>
  </section>

  <section class="spine">
    <div class="spine-text spine-authors">Dr. Reinhold Kattner, Lothar Brenning</div>
    <div class="spine-rule"></div>
    <div class="spine-text spine-title">PLAN STARK Betrieb</div>
  </section>

  <section class="front-cover">
    <div class="photo photo-factory" role="img" aria-label="Foto: Arbeiterin mit Schutzhelm und Tablet in einer Werkshalle"></div>
    <div class="photo photo-clinic" role="img" aria-label="Foto: Ärztin mit Stethoskop blickt auf ihre Armbanduhr"></div>
    <div class="photo photo-desk" role="img" aria-label="Foto: Hände am Schreibtisch mit Brille, Wecker und Laptop"></div>
    <div class="green-edge"></div>
    <div class="green-ladder"></div>
    <div class="blue-ladder"></div>
    <div class="title-block">
      <p class="front-authors">Dr. Reinhold Kattner, Lothar Brenning</p>
      <h1 class="front-title"><span class="navy">PLAN STARK</span><br><span class="green">Betrieb</span></h1>
      <p class="front-subtitle">Dienstzeiten und Schichtorganisation fair,<br>rentabel und marktnah einrichten.</p>
    </div>
    <svg class="badge" viewBox="0 0 100 100" aria-hidden="true">
      <polygon fill="#79bd27" points="98,50 87.3,57.4 94.4,68.4 81.6,71.1 83.9,83.9 71.1,81.6 68.4,94.4 57.4,87.3 50,98 42.6,87.3 31.6,94.4 28.9,81.6 16.1,83.9 18.4,71.1 5.6,68.4 12.7,57.4 2,50 12.7,42.6 5.6,31.6 18.4,28.9 16.1,16.1 28.9,18.4 31.6,5.6 42.6,12.7 50,2 57.4,12.7 68.4,5.6 71.1,18.4 83.9,16.1 81.6,28.9 94.4,31.6 87.3,42.6"/>
    </svg>
    <p class="badge-text">mit vielen<br>Praxisbeispielen</p>
    <p class="contributor">Unter Mitwirkung von Prof. Anton K. Ruhland</p>
  </section>
</body>
</html>
```